M&A Advisory firm needs elegant and powerful letterhead

We need a powerful but elegant letterhead to engage with the international financial industry.

Target Market(s)

New York and International Financial Industry

Industry/Entity Type

Finance

Font styles to use
Other font styles liked:
• Poppins

Requirements
Must have
• 482 W 71st Street 14th Floor New York, NY 10157 O: +1 (212) 555 0147 F: +1 (212) 555 0182

```html
<!DOCTYPE html>
<html lang="en">
<head>
<meta charset="utf-8">
<title>Meridane Letterhead</title>
<link href="https://fonts.googleapis.com/css2?family=Poppins:wght@400;500&display=swap" rel="stylesheet">
<style>
  :root {
    --backdrop: #dcdcdc;
    --paper: #ffffff;
    --navy: #1f4f86;
    --navy-deep: #173f6e;
    --sky: #d3e5f5;
    --sky-deep: #c3d8ec;
    --brand: #2d66a8;
    --muted: #7b8794;
    --ink: #1d2733;
  }
  * { margin: 0; padding: 0; box-sizing: border-box; }
  html, body { width: 1200px; height: 900px; overflow: hidden; background: var(--backdrop); }
  .canvas { position: relative; width: 1200px; height: 900px; display: flex; align-items: center; justify-content: center; }
  .letterhead {
    position: relative; width: 660px; height: 854px; background: var(--paper);
    box-shadow: 0 10px 30px rgba(0,0,0,.18); font-family: "Poppins", sans-serif; overflow: hidden;
  }
  .letterhead__art { position: absolute; inset: 0; width: 100%; height: 100%; }
  .brand { position: absolute; left: 34px; top: 80px; display: flex; align-items: center; gap: 12px; }
  .brand__dot { width: 26px; height: 26px; border-radius: 50%; background: var(--brand); }
  .brand__text { display: flex; flex-direction: column; }
  .brand__name { font-size: 34px; font-weight: 400; color: var(--brand); letter-spacing: 1px; line-height: 1; }
  .brand__tagline { font-size: 9px; font-weight: 400; color: var(--muted); letter-spacing: 2.6px; margin-top: 4px; margin-left: 4px; white-space: nowrap; }
  .contact-phones { position: absolute; left: 26px; top: 776px; font-size: 13px; color: var(--ink); line-height: 22px; }
  .contact-line { display: flex; align-items: center; gap: 8px; }
  .contact-line svg { width: 12px; height: 12px; fill: var(--brand); }
  .contact-address { position: absolute; right: 24px; top: 798px; display: flex; align-items: center; gap: 6px; font-size: 12.5px; color: #fff; white-space: nowrap; }
  .contact-address svg { width: 10px; height: 13px; fill: #fff; }
</style>
</head>
<body>
<main class="canvas">
  <article class="letterhead">
    <svg class="letterhead__art" viewBox="0 0 660 854" preserveAspectRatio="none">
      <defs>
        <linearGradient id="market-band" x1="0" y1="0" x2="1" y2="1">
          <stop offset="0" stop-color="#2a5f99"/>
          <stop offset="1" stop-color="#1a4475"/>
        </linearGradient>
      </defs>
      <g class="header">
        <polygon role="img" aria-label="Blue band with a faint stock market chart" fill="url(#market-band)" points="0,0 660,0 660,122 0,122"/>
        <polygon fill="var(--sky)" points="0,0 300,0 280,44 0,44"/>
        <polygon fill="#ffffff" points="0,70 320,70 345,110 320,158 0,158"/>
        <polygon fill="var(--sky)" points="0,74 316,74 340,110 316,154 0,154"/>
      </g>
      <g class="footer">
        <polygon role="img" aria-label="Blue band with a faint stock market chart" fill="url(#market-band)" points="0,854 0,770 660,750 660,854"/>
        <polygon fill="#ffffff" points="0,760 290,760 270,842 0,842"/>
        <polygon fill="var(--sky)" points="0,764 286,764 266,838 0,838"/>
        <polygon fill="#6f93b8" points="272,764 300,764 286,752"/>
      </g>
    </svg>

    <div class="brand">
      <span class="brand__dot"></span>
      <div class="brand__text">
        <span class="brand__name">MERIDANE</span>
        <span class="brand__tagline">Strategic Advisory</span>
      </div>
    </div>

    <div class="contact-phones">
      <div class="contact-line">
        <svg viewBox="0 0 24 24" aria-hidden="true"><path d="M6.6 10.8a15 15 0 0 0 6.6 6.6l2.2-2.2a1 1 0 0 1 1-.25 11.4 11.4 0 0 0 3.6.57 1 1 0 0 1 1 1V20a1 1 0 0 1-1 1A17 17 0 0 1 3 4a1 1 0 0 1 1-1h3.5a1 1 0 0 1 1 1c0 1.25.2 2.45.57 3.6a1 1 0 0 1-.25 1z"/></svg>
        <span>+1 (212) 555 0147</span>
      </div>
      <div class="contact-line">
        <svg viewBox="0 0 24 24" aria-hidden="true"><path d="M6 2h12v5H6zM4 8h16a2 2 0 0 1 2 2v6h-4v6H6v-6H2v-6a2 2 0 0 1 2-2zm4 8v4h8v-4z"/></svg>
        <span>+1 (212) 555 0182</span>
      </div>
    </div>

    <div class="contact-address">
      <svg viewBox="0 0 10 14" aria-hidden="true"><path d="M5 0a5 5 0 0 1 5 5c0 3.5-5 9-5 9S0 8.5 0 5a5 5 0 0 1 5-5zm0 3a2 2 0 1 0 0 4 2 2 0 0 0 0-4z"/></svg>
      <span>482 W 71st Street 14th Floor New York, NY 10157</span>
    </div>
  </article>
</main>
</body>
</html>
```